Poster Design For Obstacle Run

Design a poster for the Crow Ridge Obstacle run.
Text: Crow Ridge Obstacle Run. May 12th, 2018. Sittard. www.crowridgedash.nl. I have added a lot of pictures.
Furthermore, the logo should be included. As an example I included a poster from the ironbark race that we really like (ironbark team challenge) and also. Feel free to take a look at our website for inspiration: www.crowridgedash.nl

```html
<!DOCTYPE html>
<html lang="en">
<head>
<meta charset="utf-8">
<title>Crow Ridge Obstacle Run – Poster</title>
<link rel="stylesheet" href="https://fonts.googleapis.com/css2?family=Bowlby+One&family=Oswald:wght@500;600&display=swap">
<style>
  :root {
    --page-bg: #cfd8d8;
    --poster-black: #141212;
    --poster-charcoal: #221e1c;
    --accent-orange: #ec5a24;
    --text-white: #ffffff;
    --photo-light: #a8a49c;
    --photo-dark: #3a3d44;
  }
  html, body {
    margin: 0;
    width: 1200px;
    height: 1200px;
    overflow: hidden;
    background: var(--page-bg);
  }
  .poster {
    position: absolute;
    left: 190px;
    top: 25px;
    width: 820px;
    height: 1150px;
    overflow: hidden;
    background: radial-gradient(ellipse at 40% 70%, var(--poster-charcoal), var(--poster-black) 75%);
    font-family: "Oswald", sans-serif;
    color: var(--text-white);
  }
  .hero-frame {
    position: absolute;
    left: 0;
    top: 0;
  }
  .event-mark {
    position: absolute;
    top: 760px;
    left: 0;
    width: 100%;
    display: flex;
    justify-content: center;
    align-items: center;
    gap: 12px;
  }
  .event-mark__dot {
    width: 26px;
    height: 26px;
    border-radius: 50%;
    background: var(--accent-orange);
  }
  .event-mark__name {
    font-family: "Oswald", sans-serif;
    font-weight: 600;
    font-size: 40px;
    letter-spacing: 1px;
    color: var(--accent-orange);
    text-transform: uppercase;
  }
  .event-title {
    position: absolute;
    top: 872px;
    left: 0;
    width: 100%;
    margin: 0;
    text-align: center;
    font-family: "Bowlby One", sans-serif;
    font-weight: 400;
    font-size: 52px;
    line-height: 1;
    white-space: nowrap;
  }
  .event-title__name { color: var(--accent-orange); }
  .event-title__type { color: var(--text-white); text-transform: uppercase; }
  .event-location {
    position: absolute;
    top: 970px;
    left: 245px;
    width: 300px;
    height: 42px;
    display: flex;
    align-items: center;
    justify-content: center;
    gap: 14px;
    background: linear-gradient(90deg, rgba(255,255,255,0) 0%, #e8e8e8 25%, #bdbdbd 60%, rgba(255,255,255,0) 100%);
    color: var(--poster-black);
    font-weight: 600;
    font-size: 30px;
    letter-spacing: 4px;
    text-transform: uppercase;
  }
  .event-date {
    position: absolute;
    top: 1036px;
    left: 0;
    width: 100%;
    display: flex;
    justify-content: center;
    align-items: center;
    gap: 22px;
    font-weight: 600;
  }
  .event-date__stars { color: var(--text-white); font-size: 22px; letter-spacing: 4px; }
  .event-date__text { color: var(--accent-orange); font-size: 44px; text-transform: uppercase; }
  .event-url {
    position: absolute;
    top: 1106px;
    left: 0;
    width: 100%;
    text-align: center;
    font-weight: 500;
    font-size: 19px;
    letter-spacing: 7px;
    text-transform: uppercase;
  }
</style>
</head>
<body>
  <main class="poster">
    <svg class="hero-frame" width="820" height="780" viewBox="0 0 820 780">
      <defs>
        <linearGradient id="heroPhotoTone" x1="0" y1="0" x2="1" y2="1">
          <stop offset="0" stop-color="var(--photo-dark)"/>
          <stop offset="0.55" stop-color="var(--photo-light)"/>
          <stop offset="1" stop-color="#8d8a83"/>
        </linearGradient>
      </defs>
      <circle cx="420" cy="290" r="386" fill="var(--text-white)"/>
      <circle cx="424" cy="284" r="372" fill="var(--accent-orange)"/>
      <circle cx="424" cy="290" r="352" fill="url(#heroPhotoTone)" role="img" aria-label="Photo of a muddy runner vaulting over a wooden obstacle"/>
    </svg>

    <div class="event-mark">
      <span class="event-mark__dot"></span>
      <span class="event-mark__name">Crow Ridge</span>
    </div>

    <h1 class="event-title">
      <span class="event-title__name">Crow Ridge</span>
      <span class="event-title__type">Obstacle Run</span>
    </h1>

    <div class="event-location">
      <svg width="22" height="28" viewBox="0 0 22 28" aria-hidden="true">
        <path d="M11 1C5.5 1 1.5 5.2 1.5 10.4 1.5 17.5 11 27 11 27s9.5-9.5 9.5-16.6C20.5 5.2 16.5 1 11 1z" fill="none" stroke="var(--poster-black)" stroke-width="3"/>
        <circle cx="11" cy="10.5" r="3.5" fill="var(--poster-black)"/>
      </svg>
      <span>Sittard</span>
    </div>

    <div class="event-date">
      <span class="event-date__stars">★★★</span>
      <span class="event-date__text">May 12th, 2018</span>
      <span class="event-date__stars">★★★</span>
    </div>

    <div class="event-url">www.crowridgedash.nl</div>
  </main>
</body>
</html>
```